Design my Display Ad! Product for Muscle Cramps -- Need Your Talent!

I need the PSD of a square display ad to be the design concept for other ad formats. The product is for leg and muscle cramps. The ad needs to encourage clicks, not simply impressions. Image should contain legs.

Visit www.velmoristride.com for a better idea of the product.

Target Market(s)

People age 55+ with leg cramps

Industry/Entity Type

Health And Wellness

Font styles to use
Sans Serif

Colors

Designer to choose colors to be used in the design.

Requirements
Must have
• One version with the text:
• The Real Cause of Leg Cramps
• Discover the Secret
• The other version with the text:
• Leg Cramps at Night
• Discover the Real Cause
• An image focused on legs.
• Attractive presentation -- this is a premium organic brand.
• Visit www.velmoristride.com for a better understanding of the product

```html
<!DOCTYPE html>
<html lang="en">
<head>
<meta charset="utf-8">
<title>Leg Cramps at Night – Display Ad</title>
<link rel="stylesheet" href="https://fonts.googleapis.com/css2?family=Montserrat:wght@300;400;700&display=swap">
<style>
  :root {
    --green-deep: #9db53c;
    --green-light: #b6cf55;
    --sky-blue: #4fa8dc;
    --white: #ffffff;
    --ink: #141414;
  }
  html, body {
    margin: 0;
    padding: 0;
    width: 1200px;
    height: 1200px;
    overflow: hidden;
    background: var(--green-deep);
  }
  .ad {
    position: relative;
    width: 1200px;
    height: 1200px;
    overflow: hidden;
    background: var(--green-deep);
    font-family: "Montserrat", "Helvetica Neue", Arial, sans-serif;
    color: var(--white);
  }
  .ad__backdrop {
    position: absolute;
    inset: 0;
    width: 1200px;
    height: 1200px;
  }
  .ad__headline {
    position: absolute;
    right: 66px;
    top: 72px;
    margin: 0;
    text-align: right;
    line-height: 1;
  }
  .ad__headline-main {
    display: block;
    font-weight: 700;
    font-size: 146px;
    letter-spacing: 2px;
  }
  .ad__headline-sub {
    display: block;
    margin-top: 28px;
    font-weight: 300;
    font-size: 148px;
    letter-spacing: 26px;
    margin-right: -26px;
  }
  .ad__cta {
    position: absolute;
    left: 53px;
    top: 600px;
    width: 510px;
    height: 510px;
    border-radius: 50%;
    background: var(--sky-blue);
    display: flex;
    align-items: center;
    justify-content: center;
    text-align: center;
    font-weight: 400;
    font-size: 66px;
    line-height: 94px;
    letter-spacing: 1px;
  }
  .ad__visual {
    position: absolute;
    left: 627px;
    top: 480px;
    width: 513px;
    height: 518px;
    border-radius: 24px;
    background: linear-gradient(160deg, rgba(20,20,20,0.85), rgba(20,20,20,0.55));
  }
</style>
</head>
<body>
  <main class="ad">
    <svg class="ad__backdrop" viewBox="0 0 1200 1200" aria-hidden="true">
      <rect width="1200" height="1200" fill="var(--green-deep)"/>
      <polygon points="0,60 428,1200 0,1200" fill="var(--green-light)"/>
    </svg>

    <h1 class="ad__headline">
      <span class="ad__headline-main">LEG CRAMPS</span>
      <span class="ad__headline-sub">AT NIGHT</span>
    </h1>

    <div class="ad__cta">DISCOVER<br>THE REAL<br>CAUSE</div>

    <div class="ad__visual" role="img" aria-label="Pictogram of a seated person holding a cramping leg, with lightning bolts marking the pain"></div>
  </main>
</body>
</html>
```